Kem7Dex Letterhead

Need a new letterhead for my law firm.
IDENTIFYING INFORMATION BELOW:
Ansel T Brightwater III
Attorney at Law
Address: 4832 Tillbury Rd, Ste 250, Dallas, TX 75204
Phone: 866-402-7183
Fax: 469-583-0271
Email: kem@kem7dex.example
Website: www.kem7dex.example

Colors
0054AA
0677BA
7BADD7
CADEEF
E8F1F8

Requirements
Must have
• Logo needs to be on the letterhead, along with identifying information which is included in the project description.

```html
<!DOCTYPE html>
<html lang="en">
<head>
<meta charset="utf-8">
<title>Kem7Dex Letterhead</title>
<link rel="stylesheet" href="https://fonts.googleapis.com/css2?family=Arimo:wght@400;700&display=swap">
<style>
  :root {
    --navy: #0054AA;
    --ocean: #0677BA;
    --sky: #7BADD7;
    --mist: #CADEEF;
    --haze: #E8F1F8;
    --ink: #111111;
    --backdrop: #ECEDEE;
    --paper: #FFFFFF;
  }
  * { margin: 0; padding: 0; box-sizing: border-box; }
  html, body {
    width: 1200px; height: 1200px; overflow: hidden;
    background: var(--backdrop);
    font-family: "Arimo", Arial, sans-serif;
  }
  .letterhead {
    position: absolute; left: 176px; top: 0;
    width: 848px; height: 1200px;
    background: var(--paper);
    overflow: hidden;
  }
  .brand {
    position: absolute; left: 37px; top: 26px;
    font-weight: 700; font-size: 40px; letter-spacing: 3px;
    color: var(--ink); line-height: 1;
  }
  .name-band {
    position: absolute; left: 0; top: 123px;
    width: 410px; height: 50px;
  }
  .name-band svg { position: absolute; inset: 0; }
  .name-band .attorney {
    position: absolute; left: 37px; top: 4px; color: #fff;
    font-weight: 700; font-size: 19px; line-height: 1.2;
  }
  .name-band .role {
    position: absolute; left: 37px; top: 28px; color: #fff;
    font-weight: 400; font-size: 16px; line-height: 1.1;
  }
  .contact {
    position: absolute; right: 0; top: 84px; list-style: none;
  }
  .contact li {
    display: flex; align-items: center; justify-content: flex-end;
    height: 23px; font-size: 14px; color: var(--ink);
  }
  .contact .icon {
    width: 29px; height: 14px; margin-left: 11px;
    background: var(--navy);
    display: flex; align-items: center; justify-content: center;
  }
  .footer-band {
    position: absolute; left: 0; bottom: 0; width: 848px; height: 39px;
  }
  .footer-band .stripe { height: 9px; }
  .footer-band .stripe.mist { background: var(--mist); }
  .footer-band .stripe.sky { background: var(--sky); }
  .footer-band .stripe.ocean { background: var(--ocean); }
  .footer-band .stripe.navy { height: 12px; background: var(--navy); }
  .footer-band .address {
    position: absolute; left: 0; right: 0; top: 8px;
    text-align: center; color: #fff; font-weight: 700; font-size: 14px;
  }
</style>
</head>
<body>
<main class="letterhead">
  <div class="brand">KEM7DEX</div>

  <div class="name-band">
    <svg width="410" height="50" viewBox="0 0 410 50">
      <polygon points="0,0 352,0 372,50 0,50" fill="var(--navy)"/>
      <polygon points="352,0 362,0 382,50 372,50" fill="var(--ocean)"/>
      <polygon points="362,0 373,0 393,50 382,50" fill="var(--sky)"/>
      <polygon points="373,0 381,0 401,50 393,50" fill="var(--mist)"/>
      <polygon points="381,0 390,0 410,50 401,50" fill="var(--haze)"/>
    </svg>
    <div class="attorney">Ansel T Brightwater III</div>
    <div class="role">Attorney at Law</div>
  </div>

  <ul class="contact">
    <li>866-402-7183
      <span class="icon"><svg width="10" height="10" viewBox="0 0 10 10"><path d="M2 1 L4 1 L4.5 3 L3.4 4 Q4.5 6 6 6.6 L7 5.5 L9 6 L9 8 Q5 9 2 5.5 Q1 3.5 2 1Z" fill="#fff"/></svg></span>
    </li>
    <li>469-583-0271
      <span class="icon"><svg width="10" height="10" viewBox="0 0 10 10"><rect x="1" y="3" width="8" height="6.5" fill="#fff"/><rect x="3" y="0.5" width="4" height="3" fill="#fff"/><rect x="4" y="4.5" width="1" height="1" fill="var(--navy)"/><rect x="6" y="4.5" width="1" height="1" fill="var(--navy)"/><rect x="4" y="6.5" width="1" height="1" fill="var(--navy)"/><rect x="6" y="6.5" width="1" height="1" fill="var(--navy)"/></svg></span>
    </li>
    <li>kem@kem7dex.example
      <span class="icon"><svg width="11" height="11" viewBox="0 0 11 11"><circle cx="5.5" cy="5.5" r="4.6" fill="none" stroke="#fff" stroke-width="1.2"/><circle cx="5.5" cy="5.5" r="1.8" fill="none" stroke="#fff" stroke-width="1.2"/></svg></span>
    </li>
    <li>www.kem7dex.example
      <span class="icon"><svg width="11" height="11" viewBox="0 0 11 11" fill="none" stroke="#fff" stroke-width="0.9"><circle cx="5.5" cy="5.5" r="4.6"/><ellipse cx="5.5" cy="5.5" rx="2" ry="4.6"/><line x1="0.9" y1="5.5" x2="10.1" y2="5.5"/><line x1="1.6" y1="3.2" x2="9.4" y2="3.2"/><line x1="1.6" y1="7.8" x2="9.4" y2="7.8"/></svg></span>
    </li>
  </ul>

  <footer class="footer-band">
    <div class="stripe mist"></div>
    <div class="stripe sky"></div>
    <div class="stripe ocean"></div>
    <div class="stripe navy"></div>
    <div class="address">4832 Tillbury Rd, Ste 250, Dallas, TX 75204</div>
  </footer>
</main>
</body>
</html>
```